Range of Mayonise Bottles

We are wanting a Logo and Artwork for a Range of Mayonnaise’s.
There are 3 lines in total
Mayonnaise Regular
Mayonnaise and Garlic
Aioli ( Mayo and Lemon)
All 300g Upside down Style Bottle.
Image attached.
Logo: is Brindle Pantry

Target Market(s)

Supermarket Line

Requirements
Must have
• Brindle Pantry must be on all 3 lines
Pictures on Front
weight on Front
Ingredinets Only English
we will provide Nutrtioanl Info so please leave space
Barcodes I will upload
Nice to have
• Image of Mayonaise

```html
<!DOCTYPE html>
<html lang="en">
<head>
<meta charset="utf-8">
<title>Brindle Pantry Mayonnaise Regular Label</title>
<link rel="stylesheet" href="https://fonts.googleapis.com/css2?family=Yeseva+One&family=Barlow:wght@300&display=swap">
<style>
  :root {
    --page: #fefefe;
    --label-top: #000000;
    --label-bottom: #1b2155;
    --ink: #ffffff;
    --image-light: #eab493;
    --image-dark: #c9835b;
  }
  html, body {
    margin: 0;
    padding: 0;
    width: 1200px;
    height: 1200px;
    overflow: hidden;
    background: var(--page);
  }
  .label-art {
    display: block;
    width: 1200px;
    height: 1200px;
  }
  .label-body { fill: url(#labelGradient); }
  .label-frame {
    fill: none;
    stroke: var(--ink);
    stroke-width: 3;
  }
  .rule {
    stroke: var(--ink);
    stroke-width: 2;
  }
  .brand-name {
    font-family: "Yeseva One", serif;
    fill: var(--ink);
    font-size: 48px;
  }
  .product-name {
    font-family: "Yeseva One", serif;
    fill: var(--ink);
    font-size: 124px;
  }
  .variant-name {
    font-family: "Yeseva One", serif;
    fill: var(--ink);
    font-size: 58px;
  }
  .net-weight {
    font-family: "Barlow", sans-serif;
    font-weight: 300;
    fill: var(--ink);
    font-size: 36px;
  }
</style>
</head>
<body>
<svg class="label-art" viewBox="0 0 1920 1920" xmlns="http://www.w3.org/2000/svg">
  <defs>
    <linearGradient id="labelGradient" x1="0" y1="0" x2="0" y2="1">
      <stop offset="0.2" stop-color="var(--label-top)"/>
      <stop offset="1" stop-color="var(--label-bottom)"/>
    </linearGradient>
    <linearGradient id="imageGradient" x1="0" y1="0" x2="1" y2="1">
      <stop offset="0" stop-color="var(--image-light)"/>
      <stop offset="1" stop-color="var(--image-dark)"/>
    </linearGradient>
  </defs>

  <path class="label-body"
        d="M473 680 Q473 655 498 652 Q970 608 1430 651 Q1461 655 1461 686 V1276 Q1461 1300 1437 1302 Q970 1350 500 1302 Q473 1299 473 1272 Z"/>

  <path class="label-frame"
        d="M851 753 C825 753 810 689 795 689 L640 697 Q610 700 595 703 Q550 710 550 755 V1200 Q550 1250 600 1256 Q970 1294 1340 1256 Q1384 1252 1384 1210 V765 Q1384 700 1290 694 L1140 692 C1110 692 1115 753 1092 753"/>

  <g class="brand-mark">
    <text class="brand-name" x="974" y="734" text-anchor="middle" textLength="126" lengthAdjust="spacingAndGlyphs">BRINDLE</text>
    <line class="rule" x1="909" y1="748" x2="963" y2="748"/>
    <rect x="969" y="743" width="9" height="9" fill="var(--ink)" transform="rotate(45 973.5 747.5)"/>
    <line class="rule" x1="984" y1="748" x2="1039" y2="748"/>
    <text class="brand-name" x="974" y="810" text-anchor="middle" textLength="138" lengthAdjust="spacingAndGlyphs">PANTRY</text>
  </g>

  <text class="product-name" x="975" y="975" text-anchor="middle" textLength="664" lengthAdjust="spacingAndGlyphs">MAYONNAISE</text>

  <line class="rule" x1="689" y1="1033" x2="834" y2="1033"/>
  <text class="variant-name" x="980" y="1054" text-anchor="middle" textLength="236" lengthAdjust="spacingAndGlyphs">REGULAR</text>
  <line class="rule" x1="1122" y1="1033" x2="1267" y2="1033"/>

  <rect class="ingredient-image" role="img" aria-label="Illustration of three brown eggs"
        x="938" y="1093" width="84" height="70" rx="8" fill="url(#imageGradient)"/>

  <text class="net-weight" x="981" y="1235" text-anchor="middle">300g</text>
</svg>
</body>
</html>
```